Investment fund letterhead + bus.card design

We are an investment fund focused on investments in the energy sector.
Pls. use design of existing logo in the attachment.
You are free to change the colors of the logo.
However, some associations should exist on the website as well.
webpage: www.brelwickholdings.fund.
This is a contest for a letterhead and business card. Therefore, pls. present letterhead and business card at once. The winner will be selected by January 11, 12pm.

Good luck! Good luck! Good luck! Good luck! Good luck! Good luck! Good luck! Good luck! Good luck! Good luck! Good luck! Good luck! Good luck! Good luck! Good luck! Good luck! Good luck! Good luck! Good luck! Good luck! Good luck! Good luck! Good luck! Good luck! Good luck! Good luck! Good luck! Good luck! Good luck! Good luck! Good luck! Good luck! Good luck! Good luck! Good luck! Good luck! Good luck! Good luck! Good luck! Good luck! Good luck! Good luck! Good luck! Good luck! Good luck! Good luck! Good luck! Good luck! Good luck! Good luck! Good luck! Good luck! Good luck! Good luck! Good luck! Good luck! Good luck! Good luck! Good luck! Good luck! Good luck! Good luck! Good luck! Good luck! Good luck! Good luck! Good luck! Good luck! Good luck! Good luck! Good luck! Good luck! Good luck! Good luck! Good luck! Good luck! Good luck! Good luck! Good luck! Good luck! Good luck! Good luck! Good luck! Good luck! Good luck! Good luck! Good luck! Good luck! Good luck! Good luck! Good luck! Good luck! Good luck! Good luck! Good luck! Good luck! Good luck! Good luck! Good luck! Good luck! Good luck! Good luck! Good luck! Good luck! Good luck! Good luck! Good luck! Good luck! Good luck! Good luck! Good luck! Good luck! Good luck! Good luck! Good luck! Good luck! Good luck! Good luck! Good luck! Good luck! Good luck! Good luck! Good luck! Good luck! Good luck! Good luck! Good luck! Good luck! Good luck! Good luck! Good luck! Good luck! Good luck! Good luck! Good luck! Good luck! Good luck! Good luck! Good luck! Good luck! Good luck! Good luck! Good luck! Good luck! Good luck! Good luck! Good luck! Good luck! Good luck! Good luck! Good luck! Good luck! Good luck! Good luck! Good luck! Good luck! Good luck! Good luck! Good luck! Good luck! Good luck! Good luck! Good luck! Good luck! Good luck! Good luck! Good luck! Good luck! Good luck! Good luck! Good luck! Good luck! Good luck! Good luck! Good luck! Good luck! Good luck! Good luck! Good luck! Good luck! Good luck! Good luck! Good luck! Good luck! Good luck! Good luck! Good luck! Good luck! Good luck! Good luck! Good luck! Good luck! Good luck! Good luck! Good luck! Good luck! Good luck! Good luck! Good luck! Good luck! Good luck! Good luck! Good luck! Good luck! Good luck! Good luck! Good luck! Good luck! Good luck! Good luck! Good luck! Good luck! Good luck! Good luck! Good luck! Good luck! Good luck! Good luck! Good luck! Good luck! Good luck! Good luck! Good luck! Good luck! Good luck! Good luck! Good luck! Good luck! Good luck! Good luck! Good luck! Good luck! Good luck! Good luck! Good luck! Good luck! Good luck! Good luck! Good luck! Good luck! Good luck! Good luck! Good luck!

Target Market(s)

Energy companies, Financial institutions

Industry/Entity Type

Investment Banking

Contact Information for Business Card

Title, Name, contacts

Font styles to use
Serif

Colors

Designer to choose colors to be used in the design.

Requirements
Must have
• Logo
Nice to have
• Some modern design hints/design elements.

```html
<!DOCTYPE html>
<html lang="en">
<head>
<meta charset="utf-8">
<title>Brelwick Holdings – Letterhead and Business Card</title>
<link rel="stylesheet" href="https://fonts.googleapis.com/css2?family=Open+Sans:wght@400;600;700&display=swap">
<style>
  :root {
    --navy: #0c2a47;
    --grey-line: #9a9a9a;
    --text-grey: #8a8a8a;
    --paper: #ffffff;
    --backdrop: #2e2e2e;
    --faint: #eef0f2;
  }
  * { margin: 0; padding: 0; box-sizing: border-box; }
  html, body { width: 1200px; height: 904px; overflow: hidden; }
  body {
    position: relative;
    background: var(--backdrop);
    font-family: "Open Sans", Arial, sans-serif;
    color: var(--text-grey);
  }

  /* brand lockup */
  .brand { display: flex; align-items: center; gap: 7px; color: var(--navy); font-weight: 600; letter-spacing: 0.14em; white-space: nowrap; }
  .brand-square { background: var(--navy); flex: none; }

  /* footer band shared */
  .band-rule { position: absolute; left: 0; right: 0; background: var(--grey-line); }
  .band { position: absolute; left: 0; right: 0; bottom: 0; background: var(--navy); color: #fff; display: flex; align-items: center; justify-content: center; letter-spacing: 0.12em; }
  .band b { font-weight: 700; }

  /* letterhead */
  .letterhead { position: absolute; left: 421px; top: 36px; width: 597px; height: 843px; background: var(--paper); }
  .letterhead .brand { position: absolute; left: 43px; top: 58px; font-size: 13px; }
  .letterhead .brand-square { width: 26px; height: 26px; }
  .letterhead .contact { position: absolute; left: 452px; top: 60px; font-size: 9.5px; line-height: 12px; color: var(--text-grey); }
  .contact-line { display: flex; align-items: center; gap: 6px; }
  .contact-line svg { flex: none; }
  .letterhead .watermark { position: absolute; left: 176px; top: 298px; width: 246px; height: 246px; display: flex; flex-direction: column; align-items: center; justify-content: center; gap: 14px; color: var(--faint); font-weight: 700; font-size: 30px; letter-spacing: 0.1em; line-height: 1.15; text-align: center; }
  .watermark .brand-square { width: 70px; height: 70px; background: var(--faint); }
  .letterhead .band-rule { bottom: 24px; height: 2px; }
  .letterhead .band { height: 22px; font-size: 9px; }

  /* business cards */
  .card { position: absolute; left: 109px; width: 253px; height: 145px; }
  .card-front { top: 249px; background: var(--paper); }
  .card-front .brand { position: absolute; left: 18px; top: 60px; font-size: 7px; gap: 5px; }
  .card-front .brand-square { width: 12px; height: 12px; }
  .card-front .divider { position: absolute; left: 127px; top: 37px; width: 1px; height: 60px; background: #c8c8c8; }
  .card-front .person { position: absolute; left: 142px; top: 36px; }
  .person-name { color: var(--navy); font-weight: 700; font-size: 8.5px; line-height: 11px; }
  .person-title { font-size: 5.5px; line-height: 8px; margin-bottom: 5px; }
  .person-address { font-size: 5.5px; line-height: 8px; margin-bottom: 6px; }
  .person .contact-line { font-size: 5.5px; line-height: 8px; gap: 4px; }
  .card-front .band-rule { bottom: 17px; height: 2px; }
  .card-front .band { height: 15px; font-size: 6px; }

  .card-back { top: 424px; background: var(--navy); color: #fff; }
  .card-back .brand { position: absolute; left: 0; right: 0; top: 62px; justify-content: center; color: #fff; font-size: 8px; }
  .card-back .brand-square { width: 12px; height: 12px; background: #fff; }
  .card-back .web { position: absolute; left: 0; right: 0; top: 114px; text-align: center; font-size: 6px; letter-spacing: 0.12em; }
  .card-back .web b { font-weight: 700; }
</style>
</head>
<body>

<section class="letterhead" aria-label="Letterhead">
  <div class="brand"><span class="brand-square"></span>BRELWICK HOLDINGS</div>

  <address class="contact" style="font-style:normal">
    <div>48 Ardent Lane, Suite 210</div>
    <div>Marlow Park, CA 90412.</div>
    <div class="contact-line">
      <svg width="8" height="8" viewBox="0 0 10 10"><path d="M2 1 L4 1 L4.6 3.2 L3.4 4.2 Q4.6 6 6 6.8 L7 5.6 L9 6.2 L9 8.2 Q5 9 2.2 5.6 Q1 3.6 2 1Z" fill="#0c2a47"/></svg>
      <span>+1 555 014 2290</span>
    </div>
    <div class="contact-line">
      <svg width="8" height="8" viewBox="0 0 10 10"><rect x="1" y="2.5" width="8" height="5.5" fill="#0c2a47"/><path d="M1 2.5 L5 5.5 L9 2.5" stroke="#fff" stroke-width="0.8" fill="none"/></svg>
      <span>info@brelwickholdings.fund</span>
    </div>
    <div class="contact-line">
      <svg width="8" height="8" viewBox="0 0 10 10"><circle cx="5" cy="5" r="4" fill="#0c2a47"/><path d="M1 5 H9 M5 1 Q2.5 5 5 9 M5 1 Q7.5 5 5 9" stroke="#fff" stroke-width="0.6" fill="none"/></svg>
      <span>www.brelwickholdings.fund</span>
    </div>
  </address>

  <div class="watermark" aria-hidden="true">
    <span class="brand-square"></span>
    <span>BRELWICK<br>HOLDINGS</span>
  </div>

  <div class="band-rule"></div>
  <div class="band">www.<b>brelwickholdings</b>.fund</div>
</section>

<section class="card card-front" aria-label="Business card front">
  <div class="brand"><span class="brand-square"></span>BRELWICK HOLDINGS</div>
  <div class="divider"></div>
  <div class="person">
    <div class="person-name">Edwin Harrow</div>
    <div class="person-title">Manager</div>
    <div class="person-address">48 Ardent Lane, Suite 210<br>Marlow Park, CA 90412.</div>
    <div class="contact-line">
      <svg width="6" height="6" viewBox="0 0 10 10"><path d="M2 1 L4 1 L4.6 3.2 L3.4 4.2 Q4.6 6 6 6.8 L7 5.6 L9 6.2 L9 8.2 Q5 9 2.2 5.6 Q1 3.6 2 1Z" fill="#0c2a47"/></svg>
      <span>+1 555 014 2290</span>
    </div>
    <div class="contact-line">
      <svg width="6" height="6" viewBox="0 0 10 10"><rect x="1" y="2.5" width="8" height="5.5" fill="#0c2a47"/><path d="M1 2.5 L5 5.5 L9 2.5" stroke="#fff" stroke-width="0.8" fill="none"/></svg>
      <span>info@brelwickholdings.fund</span>
    </div>
  </div>
  <div class="band-rule"></div>
  <div class="band">www.<b>brelwickholdings</b>.fund</div>
</section>

<section class="card card-back" aria-label="Business card back">
  <div class="brand"><span class="brand-square"></span>BRELWICK HOLDINGS</div>
  <div class="web">www.<b>brelwickholdings</b>.fund</div>
</section>

</body>
</html>
```